Transfer Pricing Flyer

This is a technical document meant for CEOs and CFOs. Intent is to make a complex technical subject simple. I have also added our logo with this document for you to use it appropriately. you can also peruse our website for further details or write to me.

hi all have uploaded our logo to our brief. pl use the logo while designing

Reason: Not sufficient good designs have been recievved

Industry/Entity Type

Pricing

Colors
34a6d7
85cae6
cde9f5
ceddec
85abd2
0555a3
0255a3

```html
<!DOCTYPE html>
<html lang="en">
<head>
<meta charset="utf-8">
<title>Transfer Pricing Demystified – Pages 6 to 9</title>
<link href="https://fonts.googleapis.com/css2?family=Arimo:ital,wght@0,400;0,700;1,400&display=swap" rel="stylesheet">
<style>
:root{
  --blue-bright:#34a6d7;
  --blue-sky:#85cae6;
  --blue-mist:#cde9f5;
  --blue-pale:#ceddec;
  --blue-soft:#85abd2;
  --blue-deep:#0555a3;
  --heading:#5b97d2;
  --frame:#4f86c6;
  --ink:#3c3c3c;
  --ink-soft:#666;
  --table-head:#a6a6a6;
  --table-line:#9a9a9a;
  --table-fill:#f1f1f3;
  --panel-grey:#e6e6e6;
}
*{box-sizing:border-box;margin:0;padding:0}
html,body{width:1200px;height:1000px;overflow:hidden;background:#fff}
body{position:relative;font-family:"Arimo",Arial,sans-serif;color:var(--ink)}
.page-label{position:absolute;font-size:25px;color:#111;letter-spacing:-.3px}
.spread{position:absolute;border:1px solid var(--frame);background:#fff;overflow:hidden}
.spread-a{left:54px;top:44px;width:648px;height:457px}
.spread-b{left:540px;top:505px;width:645px;height:456px}
.page{position:absolute;top:0;height:100%}
.page-left{left:0;width:323px;border-right:1px solid var(--frame)}
.page-right{left:323px;width:323px}
.spread-b .page-left{width:322px}
.spread-b .page-right{left:322px;width:322px}
.block{position:absolute;font-size:6.4px;line-height:9.6px}
.block p{margin-bottom:2px}
.q{color:var(--heading);font-size:7px;line-height:9.6px;font-weight:700;margin:6px 0 4px}
.q.plain{font-weight:400}
.block b{color:#222}
.photo{position:absolute;left:174px;top:26px;width:150px;height:234px;
  background:linear-gradient(160deg,#c9d6e2 0%,#8fa3b8 35%,#d9cfa4 70%,#6f7f90 100%)}
.wedge{position:absolute;left:0;top:0}
.quote{position:absolute;left:175px;top:338px;width:130px;font-style:italic;font-size:13.5px;line-height:24px;color:#8d8d8d}
.footer{position:absolute;top:431px;font-size:5.4px;font-weight:700;color:#222}
.spread-b .footer{top:430px}
table{border-collapse:collapse;width:100%;font-size:5.6px;line-height:7px}
th{background:var(--table-head);color:#fff;font-weight:700;text-align:center;padding:2px}
td{border:1px solid var(--table-line);background:var(--table-fill);padding:1px 3px;vertical-align:middle}
.penalty{position:absolute;left:30px;top:316px;width:273px}
.penalty td{height:15px}
.penalty td.long{height:21px}
.harbour{position:absolute;left:29px;top:47px;width:272px}
.harbour td{height:18.3px}
.harbour td.c{text-align:center}
.circle{position:absolute;left:0;top:0}
.contact-title{position:absolute;left:19px;top:196px;font-size:22px;color:var(--blue-deep);letter-spacing:.2px}
.contact-intro{position:absolute;left:23px;top:227px;font-size:6.2px}
.person{position:absolute;font-size:6.4px;line-height:9px}
.person .name{color:var(--blue-deep);font-weight:700;font-size:7px}
.person .role{font-style:italic;color:#222}
.person .mail{text-decoration:underline;color:#444;font-size:5.8px}
.about{position:absolute;left:16px;top:343px;width:292px;height:95px;background:var(--panel-grey);padding:8px;font-size:4.3px;line-height:6px;color:#555}
.about .firm{font-size:6px;font-weight:700;color:#333;margin-bottom:4px}
.about .sub{font-weight:700;color:#333;font-size:5px}
.about .side{position:absolute;left:200px;top:8px;width:85px}
.about .web{font-weight:700;color:#333;font-size:5.4px;margin-top:6px}
</style>
</head>
<body>

<div class="page-label" style="left:52px;top:6px">Page 6</div>
<div class="page-label" style="left:384px;top:6px">Page 7</div>
<div class="page-label" style="left:540px;top:962px">Page 8</div>
<div class="page-label" style="left:873px;top:962px">Page 9 / End</div>

<!-- Spread: pages 6 and 7 -->
<section class="spread spread-a">
  <div class="page page-left">
    <div class="block" style="left:30px;top:22px;width:118px">
      <p>- Description of the methods considered</p>
      <p>- Record of the actual workings carried out for determining the arm's length price</p>
      <p>- Assumptions, policies and price negotiations</p>
      <p>- Details of the adjustments</p>
      <p>- Any other information, data or document as may be considered relevant</p>
      <div class="q plain" style="margin-top:10px">Is it mandatory for a transfer pricing study document to be maintained by all concerns or what is the minimum threshold for maintenance of transfer pricing documentation?</div>
      <p><b>- For domestic transactions –</b> the minimum threshold is Rs 5 crores of aggregate transactions with related concerns</p>
      <p style="margin-top:5px"><b>- For international transactions –</b> the minimum threshold is Rs 1 crore of aggregate transactions with related concerns</p>
    </div>
    <div class="block" style="left:30px;top:286px;width:290px">
      <div class="q plain">What are the consequences of non maintenance of transfer pricing documentation and non submission of Chartered Accountants report?</div>
    </div>
    <div class="penalty">
      <table>
        <tr><th>Offence</th><th>Penalty</th></tr>
        <tr><td>Non maintenance of transfer pricing records and documents</td><td>2% of the value of the transaction with related concern</td></tr>
        <tr><td>Failure to furnish report of a chartered accountant</td><td>Rs 1 lakh</td></tr>
        <tr><td class="long">Failure to furnish documents to the Assessing officer or Commissioner Appeals</td><td>2% of the value of the transaction with related concern</td></tr>
      </table>
    </div>
    <div class="footer" style="left:27px">6 | Transfer Pricing Demystified</div>
    <div class="footer" style="right:18px">Kestrel Vale Advisors LLP | www.kestrelvale.in</div>
  </div>

  <div class="page page-right">
    <div class="block" style="left:24px;top:20px;width:136px">
      <div class="q plain" style="margin-top:4px">An assessee has conducted a related party sale transaction at Rs 100 per unit however the arm's length price after verifying the records and comparable transactions is Rs 105 per unit. What would be the implications?</div>
      <p>Where there is a difference between the transaction price and arm's length price, such difference shall be referred to as "Transfer pricing adjustment". Transfer pricing adjustment is generally a direct addition to the net income of the assessee and no deductions are available on such adjustment.</p>
      <p>In this case, the difference between of Rs 5 shall be regarded as transfer pricing adjustment.</p>
      <div class="q plain">Is there any change in implications if the transfer pricing adjustment is mandated consequent to a conclusion framed by the income tax department?</div>
      <p>Transfer pricing adjustments are of two types:</p>
      <p><b>- Adjustments made by the assessee voluntarily:</b> In this case the amount of adjustment shall be directly added to the net income of the assessee.</p>
      <p style="margin-top:5px"><b>- Adjustments made by the department:</b> In this case the amount of adjustment shall be directly added to the net income of the assessee. Simultaneously penal proceedings may be initiated against the assessee by the tax department.</p>
    </div>
    <div class="block" style="left:172px;top:20px;width:132px">
      <p style="margin-top:4px"><b>- Is there any assurance that once a transfer pricing study is done, there would be no further adjustment by the income tax department?</b></p>
      <p>A transfer pricing study document is, in our opinion, the arm's length price of the transaction under consideration. The document is a mandatory compliance which needs to be adopted and must be scientifically done to ensure the arm's length price determined. However there are many areas of subjectivity involved in a transfer pricing study while determining the arm's length price. Hence a transfer pricing study may not be an assurance from litigation however the assessee has a great case to defend if the transfer pricing study is comprehensive.</p>
      <div class="q plain">Is there a simpler way of complying with Transfer pricing regulations?</div>
      <p>Yes, the Income tax department has recently introduced safe harbour regulations wherein concerns operating in certain specified industries can avail the benefit of simplified compliance if they offer the margins prescribed in the rules.</p>
    </div>
    <p class="quote">“ A transfer pricing study may not be an assurance from litigation ”</p>
    <div class="footer" style="left:22px">Kestrel Vale Advisors LLP | www.kestrelvale.in</div>
    <div class="footer" style="right:20px">Transfer Pricing Demystified | 7</div>
  </div>

  <div class="photo" role="img" aria-label="Photograph of a family shopping in a bright supermarket aisle"></div>
  <svg class="wedge" width="648" height="457" aria-hidden="true">
    <defs>
      <linearGradient id="wedgeFade" x1="0" y1="0" x2="1" y2="0">
        <stop offset="0" stop-color="#34a6d7" stop-opacity=".85"/>
        <stop offset="1" stop-color="#85cae6" stop-opacity=".35"/>
      </linearGradient>
    </defs>
    <polygon points="318,0 350,0 330,260 305,260" fill="url(#wedgeFade)"/>
  </svg>
</section>

<!-- Spread: pages 8 and 9 -->
<section class="spread spread-b">
  <svg class="circle" width="645" height="456" aria-hidden="true">
    <circle cx="356" cy="55" r="145" fill="var(--blue-mist)"/>
  </svg>

  <div class="page page-left" style="border-right-color:var(--frame)">
    <div class="block" style="left:29px;top:18px;width:272px">
      <div class="q plain" style="margin-top:4px">What are the industries and the respective margins specified for the purpose of Safe Harbour Rules?</div>
    </div>
    <div class="harbour">
      <table>
        <tr><th style="width:136px">Eligible International Assessee</th><th>Circumstance</th><th style="width:65px">Limit</th></tr>
        <tr><td rowspan="3">Software development services / ITES</td><td>Value of transaction</td><td>Operating margin / Rate charged</td></tr>
        <tr><td>Up to Rs 500 crores</td><td class="c">&gt;= 20%</td></tr>
        <tr><td>Above Rs 500 crores</td><td class="c">&gt;= 22%</td></tr>
        <tr><td>KPO Services</td><td>No limit</td><td class="c">&gt;= 25%</td></tr>
        <tr><td>Contract R&amp;D services, relating to software development</td><td>No limit</td><td class="c">&gt;= 25%</td></tr>
        <tr><td>Contract R&amp;D services, relating to generic pharmaceutical drugs</td><td>No limit</td><td class="c">&gt;= 25%</td></tr>
        <tr><td>Manufacture and export of Core auto components</td><td>No limit</td><td class="c">&gt;= 12%</td></tr>
        <tr><td>Manufacture and export of non core auto components</td><td>No limit</td><td class="c">&gt;= 8.5%</td></tr>
        <tr><td rowspan="2">Intra group loans</td><td>Up to Rs 50 crores</td><td>Base rate of NCB plus 150 basis points</td></tr>
        <tr><td>Beyond Rs 50 crores</td><td>Base rate of NCB plus 300 basis points</td></tr>
        <tr><td rowspan="2">Corporate Guarantee</td><td>Up to Rs 100 crores</td><td class="c">2%</td></tr>
        <tr><td>Beyond Rs 100 crores</td><td class="c">1.75%</td></tr>
      </table>
    </div>
    <div class="block" style="left:29px;top:298px;width:272px">
      <div class="q plain">Is there any change in implications if the transfer pricing adjustment is mandated consequent to a conclusion framed by the income tax department?</div>
      <p>Yes, even where an assessee opts for the simpler scheme of safe harbour, it is mandatory for the assessee to maintain the transfer pricing documentation.</p>
      <div class="q plain">Is there a way to have certainty in transfer pricing assessment?</div>
      <p>Yes, there is an option called "Advance Pricing Agreement". An advance pricing agreement is a prior agreement between the income tax department and the tax payer assessee about the international transaction under consideration. Through this agreement, both the assessee and the department agree on the commercial terms and conditions including the pricing and resultant taxable margins in India. An advance pricing agreement lends substantial certainty to the entire process of transfer pricing assessments.</p>
    </div>
    <div class="footer" style="left:27px">8 | Transfer Pricing Demystified</div>
    <div class="footer" style="right:20px">Kestrel Vale Advisors LLP | www.kestrelvale.in</div>
  </div>

  <div class="page page-right">
    <div class="block" style="left:24px;top:18px;width:126px">
      <div class="q plain" style="margin-top:4px">How long does it take for obtaining an advance pricing agreement?</div>
      <p>Advance pricing agreement regime in India is still new and is evolving. India is one of the latest entrants in this space and is already doing well compared many developed economies. Based on our past experience and interactions with the department, we are of the opinion that it would take atleast 12-18 months for successful conclusion of an advance pricing agreement.</p>
    </div>
    <div class="block" style="left:171px;top:18px;width:128px">
      <div class="q plain" style="margin-top:4px">Is advance pricing agreement an option available to all assessees subject to</div>
      <p>The law does not restrict the applicability advance pricing agreements to a certain section of the assessees. However, given the initial statutory costs involved, we are of the opinion that advance pricing agreements would make commercial sense if the value of the international related transactions exceeds Rs 20 crore annually.</p>
    </div>

    <h2 class="contact-title">CONTACT US</h2>
    <p class="contact-intro">For any further assistance please feel to get in touch with our team of specialists.</p>

    <div class="person" style="left:24px;top:250px">
      <div class="name">Arun Mehrotra</div>
      <div class="role">Managing Partner</div>
      <div class="mail">arun@kestrelvale.in</div>
    </div>
    <div class="person" style="left:163px;top:250px">
      <div class="name">Kiran.P</div>
      <div class="role">Partner</div>
      <div class="mail">kiran@kestrelvale.in</div>
    </div>
    <div class="person" style="left:24px;top:292px">
      <div class="name">Meera Ranganathan</div>
      <div class="role">Partner</div>
      <div class="mail">meera@kestrelvale.in</div>
    </div>
    <div class="person" style="left:163px;top:292px">
      <div class="name">Rohan Desai</div>
      <div class="role">International Relations</div>
      <div class="mail">rohan@kestrelvale.in</div>
    </div>

    <div class="about">
      <div class="firm">Kestrel Vale Advisors LLP | Tax | Legal | Forensic</div>
      <div class="sub">About Kestrel Vale Advisors</div>
      <p style="width:180px">Kestrel Vale Advisors is a contemporary tax and advisory firm focused on providing value added services to its clientele. The firm offers multidisciplinary solutions spanning across conventional and contemporary solutions covering multiple aspects of domestic and international taxation. The firm has a team of over 50 professionals spread across 7 offices in India, Middle East and Singapore.</p>
      <p style="width:180px;margin-top:5px">The firm is a member of Northgate Global Alliance, one of the top 20 accounting and legal associations in the world having affiliates in over 100 countries.</p>
      <div class="side">
        <p>© 2014 Kestrel Vale Advisors LLP<br>All Rights Reserved.</p>
        <p class="web">www.kestrelvale.in</p>
      </div>
    </div>
  </div>
</section>

</body>
</html>
```